Harrowgate Building and Property Services needs a business card design

We need a business card design for our building and property services business. We already have a logo we just need a creative design and layout on a business card. Emphasis on clean, modern, professional.
Our client targets are mainly body corporates, building managers, construction managers.
We are a building services company that lean more to structural repair of buildings, through concrete rectification and carbon fibre strengthening.
We also refurbish facades, rendering, painting etc
We target higher end body corporates in prestigious locations, hence why we'd like our cards to reflect professionalism, strength, efficiency

Target Market(s)

body corporates, building managers, construction managers

Industry/Entity Type

Construction

Contact Information for Business Card

Harrowgate is the main word, with 'Building and Property Services' underneath.
Level 17, 88 Marsh Lane
ELMSWORTH
Melbourne
Vic 3942
T: 9218 5371
Duncan Hensley - Director
dunharrowgate@mailbox-example.net

Requirements
Must have
• Stand out on the back of the card- strong/ bold, company logo
• All of the contact details written above
Should not have
• I'd like the card to stand out, especially on the back. Id like the company logo to be prominent, although feel free to be creative around it. But remain clean and professional

```html
<!DOCTYPE html>
<html lang="en">
<head>
<meta charset="UTF-8">
<title>Harrowgate Building and Property Services – Business Card</title>
<link rel="stylesheet" href="https://fonts.googleapis.com/css2?family=Cinzel:wght@500&family=Montserrat:wght@400;500&display=swap">
<style>
  :root {
    --page-bg: #e9eaec;
    --card-white: #ffffff;
    --brand-blue: #1e8ad6;
    --deep-blue: #1b4a8f;
    --panel-grey: #a9aaac;
    --stripe-grey: #c4c5c7;
    --text-grey: #8a8b8e;
    --text-white: #ffffff;
  }
  * { margin: 0; padding: 0; box-sizing: border-box; }
  html, body {
    width: 1200px; height: 900px; overflow: hidden;
    background: var(--page-bg);
  }
  .canvas { position: relative; width: 1200px; height: 900px; }

  .card {
    position: absolute;
    width: 520px; height: 318px;
    background: var(--card-white);
    box-shadow: 0 6px 18px rgba(0,0,0,0.18);
    overflow: hidden;
  }
  .card--front { left: 100px; top: 90px; }
  .card--back  { left: 580px; top: 480px; }

  .brand-name {
    font-family: "Cinzel", serif;
    font-weight: 500;
    color: var(--brand-blue);
    letter-spacing: 2px;
    line-height: 1;
  }
  .brand-tagline {
    font-family: "Cinzel", serif;
    font-weight: 500;
    color: var(--text-grey);
    letter-spacing: 1.2px;
    text-transform: uppercase;
    line-height: 1;
  }

  /* Front */
  .front-lockup {
    position: absolute; inset: 0;
    display: flex; flex-direction: column;
    align-items: center; justify-content: center;
    gap: 8px;
  }
  .front-lockup .brand-name { font-size: 38px; }
  .front-lockup .brand-tagline { font-size: 10.5px; }

  /* Back */
  .back-shapes { position: absolute; inset: 0; }
  .back-lockup {
    position: absolute; right: 22px; top: 26px;
    text-align: right;
  }
  .back-lockup .brand-name { font-size: 46px; }
  .back-lockup .brand-tagline { font-size: 12.5px; margin-top: 6px; }

  .contact {
    position: absolute; right: 22px; top: 140px;
    text-align: right;
    font-family: "Montserrat", sans-serif;
    color: var(--text-white);
    font-size: 12px; line-height: 1.45;
  }
  .contact__name {
    font-size: 16px; font-weight: 500;
    color: var(--deep-blue);
    letter-spacing: 0.6px;
    text-transform: uppercase;
  }
  .contact__role { margin-bottom: 10px; }
  .contact__line { display: flex; justify-content: flex-end; align-items: center; gap: 6px; }
  .contact__icon { width: 10px; height: 10px; flex: none; }
  .contact__address { margin-top: 2px; }
</style>
</head>
<body>
<main class="canvas">

  <section class="card card--front" aria-label="Business card front">
    <div class="front-lockup">
      <div class="brand-name">HARROWGATE</div>
      <div class="brand-tagline">Building and Property Services</div>
    </div>
  </section>

  <section class="card card--back" aria-label="Business card back">
    <svg class="back-shapes" viewBox="0 0 520 318" width="520" height="318" aria-hidden="true">
      <rect width="520" height="318" fill="var(--card-white)"/>
      <polygon points="210,118 520,118 520,318 150,318" fill="var(--panel-grey)"/>
      <polygon points="58,118 96,118 176,318 138,318" fill="var(--stripe-grey)"/>
      <polygon points="0,118 44,118 124,318 0,318" fill="var(--deep-blue)"/>
      <polygon points="44,118 52,118 132,318 124,318" fill="var(--card-white)"/>
    </svg>

    <div class="back-lockup">
      <div class="brand-name">HARROWGATE</div>
      <div class="brand-tagline">Building and Property Services</div>
    </div>

    <div class="contact">
      <div class="contact__name">Duncan Hensley</div>
      <div class="contact__role">Director</div>
      <div class="contact__line">
        <span>9218 5371</span>
        <svg class="contact__icon" viewBox="0 0 10 10" aria-hidden="true">
          <path d="M2 0.8 L3.6 0.8 L4.2 3 L3 3.8 Q4 6 6.2 7 L7 5.8 L9.2 6.4 L9.2 8 Q9.2 9.2 8 9.2 Q1 8.6 0.8 2 Q0.8 0.8 2 0.8 Z" fill="var(--deep-blue)"/>
        </svg>
      </div>
      <div class="contact__line">
        <span>dunharrowgate@mailbox-example.net</span>
        <svg class="contact__icon" viewBox="0 0 10 10" aria-hidden="true">
          <rect x="0.6" y="2" width="8.8" height="6.2" fill="none" stroke="var(--deep-blue)" stroke-width="1"/>
          <polyline points="0.8,2.2 5,5.6 9.2,2.2" fill="none" stroke="var(--deep-blue)" stroke-width="1"/>
        </svg>
      </div>
      <div class="contact__address">
        Level 17, 88 Marsh Lane<br>
        ELMSWORTH<br>
        Melbourne, Vic 3942
      </div>
    </div>
  </section>

</main>
</body>
</html>
```